Meridale Bidding Collective Website

We are an food equipment auction company and are in need of an updated website. Old website found here: http://meridalebiddingcollective.example/ . We need to be able to share upcoming auctions, past auctions, companies we've worked with, needs to be mobile friendly. We will also need an easy to access back office where we can add new info, auction info, etc.

Target Market(s)

Equipment auctions, large food manufacturers, equipment resalers

Industry/Entity Type

Auction

Coding

Coded - Design and coding required

Number of Pages Required

5+ page

Font styles to use
Sans Serif

Colors
acd136
ffffff

Requirements
Must have
• Back office where we can add new auctions
-mobile friendly
-contact us page,
-services page
-social media widgets
-must match our current logo
-current auctions on front page
- join mailing list
- past auctions / current auctions pages
Nice to have
• Would like it to be clean design, easy to view and find options, modern

```html
<!DOCTYPE html>
<html lang="en">
<head>
<meta charset="utf-8">
<title>Meridale Bidding Collective</title>
<link href="https://fonts.googleapis.com/css2?family=Barlow:wght@400;500;600;700&family=Fira+Sans:wght@400;500&display=swap" rel="stylesheet">
<style>
:root{
  --green:#8cc63f;
  --green-bright:#acd136;
  --green-dark:#77b22d;
  --ink:#3d3d3d;
  --text:#555;
  --muted:#888;
  --white:#fff;
  --grey-bg:#f0f0f0;
  --footer:#5f5f5f;
  --pill:#444;
}
*{box-sizing:border-box;margin:0;padding:0}
html,body{width:1200px;height:4383px;overflow:hidden}
body{font-family:"Fira Sans",sans-serif;color:var(--text);background:var(--white);position:relative}
section,header,footer{position:absolute;left:0;width:1200px}
.abs{position:absolute}
.heading{font-family:"Barlow",sans-serif;font-weight:600;font-size:36px;color:var(--ink);text-align:center;width:100%}
.heading span{color:var(--green)}
.heading-rule{position:absolute;left:580px;width:40px;height:3px;background:var(--green)}

/* header */
.site-header{top:0;height:140px;background:var(--white)}
.brand{left:112px;top:40px;display:flex;align-items:center;gap:14px}
.brand-square{width:54px;height:54px;background:var(--green)}
.brand-name{font-family:"Barlow",sans-serif;font-weight:600;font-size:24px;line-height:26px;color:var(--ink);width:240px}
.nav a{position:absolute;top:64px;font-family:"Barlow",sans-serif;font-weight:500;font-size:14px;color:var(--ink);text-decoration:none}
.nav a.active{color:var(--green)}

/* hero */
.hero{top:140px;height:723px;background:linear-gradient(160deg,#6f6e6a 0%,#4d4c49 45%,#3a3936 100%)}
.hero-photo{position:absolute;inset:0;background:linear-gradient(90deg,rgba(90,90,85,.6),rgba(140,140,135,.35) 70%,rgba(60,60,58,.6))}
.hero-title{top:222px;width:100%;text-align:center;font-family:"Barlow",sans-serif;color:var(--white);font-weight:500}
.hero-title .l1{font-size:60px;line-height:66px;display:block}
.hero-title .l2{font-size:76px;line-height:84px;display:block}
.hero-sub{top:384px;width:100%;text-align:center;font-family:"Barlow",sans-serif;font-weight:500;font-size:28px;line-height:42px;color:var(--white)}
.btn{display:flex;align-items:center;justify-content:center;border-radius:30px;background:var(--green);color:var(--white);font-family:"Barlow",sans-serif;font-weight:500;text-decoration:none}
.hero-btn{left:511px;top:488px;width:178px;height:56px;font-size:18px}

/* services */
.services{top:863px;height:793px}
.services-sub{top:124px;width:100%;text-align:center;font-size:16px;color:var(--text)}
.svc-label{position:absolute;font-family:"Barlow",sans-serif;font-weight:500;font-size:21px;line-height:28px;color:var(--green)}
.svc-label.dark{color:var(--ink)}

/* auctions */
.auctions{top:1656px;height:800px;background:linear-gradient(180deg,#86c43c,#8cc63f 50%,#83c039)}
.auctions .heading{color:var(--white);top:36px;position:absolute}
.tab{position:absolute;top:126px;font-family:"Barlow",sans-serif;font-weight:500;font-size:14px;color:var(--white)}
.tab-rule{left:332px;top:165px;width:168px;height:3px;background:var(--white)}
.card{position:absolute;width:471px;height:218px;background:var(--white);border-radius:3px}
.card-img{position:absolute;left:5px;top:6px;width:201px;height:206px}
.card-body{position:absolute;left:228px;top:20px;width:232px}
.card-title{font-family:"Barlow",sans-serif;font-weight:600;font-size:15px;line-height:24px;color:var(--ink);height:76px}
.card-date{font-size:14px;color:var(--muted);margin-top:2px}
.card-loc{font-size:14px;color:var(--green);margin-top:8px}
.card-btns{display:flex;gap:7px;margin-top:14px}
.card-btns span{background:var(--green);color:var(--white);font-family:"Barlow",sans-serif;font-weight:600;font-size:11px;height:36px;display:flex;align-items:center;padding:0 9px}
.view-all{left:497px;top:695px;width:206px;height:64px;background:var(--pill);font-size:17px}

/* faq */
.faq{top:2456px;height:633px}
.faq-item{position:absolute;left:220px;width:760px;border:1px solid #ddd;border-radius:27px;box-shadow:0 3px 6px rgba(0,0,0,.12);background:var(--white)}
.faq-q{position:absolute;left:24px;top:15px;font-size:16px;color:var(--text)}
.faq-ico{position:absolute;right:20px;top:16px}
.faq-a{position:absolute;left:28px;top:56px;width:620px;font-size:13px;line-height:22px;font-style:italic;color:var(--muted)}

/* equipment finder */
.finder{top:3089px;height:592px;background:var(--grey-bg)}
.finder-img{left:155px;top:56px;width:449px;height:468px;background:linear-gradient(120deg,#7d848c,#c5c9cd 45%,#8e9399 70%,#b9bcc0)}
.finder-title{left:657px;top:112px;font-family:"Barlow",sans-serif;font-weight:600;font-size:34px;color:var(--ink)}
.finder-title span{color:var(--green)}
.finder-rule{left:657px;top:168px;width:52px;height:3px;background:#777}
.finder-text{left:657px;width:432px;font-size:13px;line-height:23px;color:var(--text)}
.finder-btn{left:657px;top:400px;width:194px;height:62px;font-size:19px}

/* partners */
.partners{top:3681px;height:213px;background:var(--white)}
.partner{position:absolute;top:57px;width:181px;height:103px;border:4px solid #f2f2f2;display:flex;align-items:center;justify-content:center;font-family:"Barlow",sans-serif;font-weight:500;font-size:24px;color:#a9a9a9}

/* footer */
.site-footer{top:3894px;height:489px;background:var(--footer);color:var(--white)}
.foot-brand{left:112px;top:72px;display:flex;align-items:center;gap:14px}
.foot-brand .brand-square{background:var(--white);width:50px;height:50px}
.foot-brand .brand-name{color:var(--white)}
.foot-about{left:112px;top:150px;width:318px;font-size:12px;line-height:24px;text-align:justify}
.foot-h{font-family:"Barlow",sans-serif;font-weight:500;font-size:19px}
.contact-line{position:absolute;left:528px;font-size:14px;line-height:23px;letter-spacing:.4px}
.contact-ico{position:absolute;left:488px}
.foot-signup{left:766px;top:122px;width:323px;font-size:13px;line-height:22px}
.foot-input{left:766px;top:186px;width:323px;height:41px;background:var(--white);border-radius:3px;color:#777;font-size:14px;padding:11px 18px}
.foot-sub{left:766px;top:244px;width:136px;height:41px;font-size:14px}
.foot-rule{left:112px;top:364px;width:976px;height:1px;background:#777}
.social{position:absolute;top:388px;width:38px;height:38px;border:2px solid var(--white);border-radius:50%}
.copyright{top:452px;width:100%;text-align:center;font-size:15px}
</style>
</head>
<body>

<header class="site-header">
  <div class="abs brand"><div class="brand-square"></div><div class="brand-name">Meridale Bidding Collective</div></div>
  <nav class="nav">
    <a class="active" style="left:482px">HOME</a>
    <a style="left:560px">SERVICES</a>
    <a style="left:664px">FAQ'S</a>
    <a style="left:742px">AUCTIONS</a>
    <a style="left:851px">EQUIPMENT FINDER</a>
    <a style="left:1025px">CONTACT</a>
  </nav>
</header>

<section class="hero">
  <div class="hero-photo" role="img" aria-label="Food manufacturing floor with workers in hairnets and a large stainless steel filling machine"></div>
  <h1 class="abs hero-title"><span class="l1">MERIDALE</span><span class="l2">BIDDING COLLECTIVE</span></h1>
  <p class="abs hero-sub">LEADERS IN FOOD MANUFACTURING &amp; PACKAGING<br>EQUIPMENT AUCTIONS</p>
  <a class="abs btn hero-btn">READ MORE</a>
</section>

<section class="services">
  <h2 class="abs heading" style="top:48px">OUR <span>SERVICES</span></h2>
  <div class="heading-rule" style="top:101px"></div>
  <p class="abs services-sub">Below are a list of our services please contact us for more information.</p>
  <svg class="abs" style="left:0;top:0" width="1200" height="793" viewBox="0 863 1200 793" fill="none" stroke="#8cc63f" stroke-width="2">
    <polygon points="403,1317 499,1146 697,1146 793,1317 697,1489 499,1489"/>
    <polygon points="425,1317 510,1171 689,1171 774,1317 689,1464 510,1464"/>
    <polyline points="458,1094 560,1094 560,1146"/>
    <polyline points="747,1096 645,1096 645,1146"/>
    <line x1="364" y1="1317" x2="403" y2="1317"/>
    <line x1="793" y1="1317" x2="844" y2="1317"/>
    <polyline points="458,1545 560,1545 560,1489"/>
    <polyline points="758,1545 645,1545 645,1489"/>
    <g fill="#fff"><circle cx="414" cy="1094" r="44"/><circle cx="791" cy="1096" r="44"/><circle cx="802" cy="1545" r="44"/><circle cx="414" cy="1545" r="44"/></g>
    <g fill="#fff" stroke="#555"><circle cx="320" cy="1317" r="44"/><circle cx="888" cy="1317" r="44"/></g>
    <g stroke="#8cc63f" stroke-width="1.6">
      <rect x="400" y="1078" width="22" height="28"/><line x1="405" y1="1086" x2="416" y2="1086"/><line x1="405" y1="1092" x2="412" y2="1092"/><circle cx="421" cy="1101" r="7"/><line x1="426" y1="1106" x2="433" y2="1113"/>
      <circle cx="791" cy="1096" r="17"/><line x1="783" y1="1106" x2="799" y2="1086"/><circle cx="784" cy="1089" r="3"/><circle cx="798" cy="1103" r="3"/>
      <rect x="400" y="1540" width="12" height="22"/><rect x="414" y="1534" width="12" height="28"/><path d="M420 1530v-18m-6 6l6-6 6 6"/>
      <rect x="784" y="1528" width="26" height="32"/><circle cx="810" cy="1556" r="9"/><circle cx="810" cy="1556" r="3"/>
    </g>
    <g stroke="#555" stroke-width="1.6">
      <rect x="313" y="1296" width="14" height="10"/><path d="M320 1306v6M304 1318v-6h32v6M320 1312v6"/><circle cx="304" cy="1324" r="5"/><circle cx="320" cy="1324" r="5"/><circle cx="336" cy="1324" r="5"/>
      <path d="M872 1318l16-15 16 15M876 1315v16h24v-16"/><rect x="884" y="1320" width="8" height="11"/>
    </g>
    <text x="599" y="1306" text-anchor="middle" fill="#555" stroke="none" font-family="Barlow, sans-serif" font-weight="600" font-size="24">MERIDALE</text>
    <text x="599" y="1338" text-anchor="middle" fill="#8cc63f" stroke="none" font-family="Barlow, sans-serif" font-weight="600" font-size="24">BIDDING</text>
  </svg>
  <div class="svc-label" style="left:247px;top:216px;width:100px;text-align:right">Appraisals</div>
  <div class="svc-label" style="left:856px;top:202px">Orderly<br>Negotiated Sales</div>
  <div class="svc-label dark" style="left:50px;top:440px;width:200px;text-align:right">Asset Management</div>
  <div class="svc-label dark" style="left:953px;top:440px">Real Estate</div>
  <div class="svc-label" style="left:254px;top:668px;width:100px;text-align:right">Auctions</div>
  <div class="svc-label" style="left:863px;top:670px">Turnkey Operations</div>
</section>

<section class="auctions">
  <h2 class="heading">OUR AUCTIONS</h2>
  <div class="tab" style="left:338px">UPCOMING AUCTIONS</div>
  <div class="tab" style="left:548px">PAST AUCTIONS</div>
  <div class="tab" style="left:716px">CURRENT AUCTIONS</div>
  <div class="abs tab-rule"></div>
  <svg class="abs" style="left:408px;top:159px" width="16" height="8"><polygon points="0,8 8,0 16,8" fill="#fff"/></svg>

  <article class="card" style="left:111px;top:206px">
    <div class="card-img" role="img" aria-label="Bakery plant interior with a long conveyor oven line" style="background:linear-gradient(135deg,#9b8f82,#c9b9a6 50%,#7e6e5c)"></div>
    <div class="card-body">
      <div class="card-title">250,000 sq. ft. Baguette, Bun &amp; Bread Equipment: Plant Closure of Hearthline Breads</div>
      <div class="card-date">5/12/2021 10:00 AM</div>
      <div class="card-loc">Chelsea , MA</div>
      <div class="card-btns"><span>VIEW DETAILS</span><span>ONLINE AUCTION</span></div>
    </div>
  </article>
  <article class="card" style="left:618px;top:206px">
    <div class="card-img" role="img" aria-label="Warehouse floor with blue packaging machinery" style="background:linear-gradient(135deg,#6f7a8a,#4a6fa8 55%,#8b8f95)"></div>
    <div class="card-body">
      <div class="card-title">Surplus Assets to National Premium Dessert Supplier and Bakery Producer</div>
      <div class="card-date">1/20/2021 10:00 AM</div>
      <div class="card-loc">Multi Location California &amp; , CO</div>
      <div class="card-btns"><span>VIEW DETAILS</span><span>ONLINE AUCTION</span></div>
    </div>
  </article>
  <article class="card" style="left:111px;top:441px">
    <div class="card-img" role="img" aria-label="Meat processing room with stainless tables" style="background:linear-gradient(135deg,#a3a6a6,#d6d8d6 50%,#8a8d8c)"></div>
    <div class="card-body">
      <div class="card-title">Meat Processing Plant Closure: Producer of links, patties, hot dogs, steaks &amp; more!</div>
      <div class="card-date">12/3/2020 10:00 AM</div>
      <div class="card-loc">Cedar Rapids, IA</div>
      <div class="card-btns"><span>VIEW DETAILS</span><span>ONLINE AUCTION</span></div>
    </div>
  </article>
  <article class="card" style="left:618px;top:441px">
    <div class="card-img" role="img" aria-label="Stainless steel bagel production machine" style="background:linear-gradient(135deg,#5a5550,#a19a90 50%,#6b6258)"></div>
    <div class="card-body">
      <div class="card-title">Complete Liquidation of Bagel Operation - Prairie Loaf International</div>
      <div class="card-date">11/19/2020 10:00 AM</div>
      <div class="card-loc">Medford, MA</div>
      <div class="card-btns"><span>VIEW DETAILS</span><span>ONLINE AUCTION</span></div>
    </div>
  </article>
  <a class="abs btn view-all">VIEW AUCTIONS</a>
</section>

<section class="faq">
  <h2 class="abs heading" style="top:56px">OUR <span>FAQS</span></h2>
  <div class="heading-rule" style="top:110px"></div>
  <div class="faq-item" style="top:143px;height:53px"><div class="faq-q">This is my first time bidding at one of your auctions. What do I need to do?</div><svg class="faq-ico" width="22" height="22"><circle cx="11" cy="11" r="11" fill="#8cc63f"/><path d="M9 6l5 5-5 5" stroke="#fff" stroke-width="2" fill="none"/></svg></div>
  <div class="faq-item" style="top:213px;height:54px"><div class="faq-q">I'd like to preview the equipment, when is that available?</div><svg class="faq-ico" width="22" height="22"><circle cx="11" cy="11" r="11" fill="#8cc63f"/><path d="M9 6l5 5-5 5" stroke="#fff" stroke-width="2" fill="none"/></svg></div>
  <div class="faq-item" style="top:283px;height:54px"><div class="faq-q">What forms of payment do you accept at your auctions?</div><svg class="faq-ico" width="22" height="22"><circle cx="11" cy="11" r="11" fill="#8cc63f"/><path d="M9 6l5 5-5 5" stroke="#fff" stroke-width="2" fill="none"/></svg></div>
  <div class="faq-item" style="top:356px;height:52px"><div class="faq-q">What is a bank letter of credit?</div><svg class="faq-ico" width="22" height="22"><circle cx="11" cy="11" r="11" fill="#8cc63f"/><path d="M9 6l5 5-5 5" stroke="#fff" stroke-width="2" fill="none"/></svg></div>
  <div class="faq-item" style="top:426px;height:131px"><div class="faq-q">When am I required to pay for my purchased items?</div><svg class="faq-ico" width="22" height="22"><circle cx="11" cy="11" r="11" fill="#8cc63f"/><path d="M6 9l5 5 5-5" stroke="#fff" stroke-width="2" fill="none"/></svg><div class="faq-a">Invoices will be sent no later than the morning following the sale. Payment must be received within 2 business days.</div></div>
</section>

<section class="finder">
  <div class="abs finder-img" role="img" aria-label="Tall stainless steel processing tanks with insulated piping"></div>
  <h2 class="abs finder-title">EQUIPMENT <span>FINDER</span></h2>
  <div class="abs finder-rule"></div>
  <p class="abs finder-text" style="top:199px">Looking for a specific piece of equipment or even a package? We can help you! Our knowledgeable and experienced team has developed many contacts in the food and beverage industry over the years.</p>
  <p class="abs finder-text" style="top:298px;text-align:justify">Please take a minute to fill out this form. We may have what you are looking for in an upcoming auction. If we do not, we have great resources that may have exactly what you are looking for.</p>
  <a class="abs btn finder-btn">READ MORE</a>
</section>

<section class="partners">
  <svg class="abs" style="left:44px;top:80px" width="18" height="56"><path d="M16 2L2 28l14 26" stroke="#ccc" stroke-width="2" fill="none"/></svg>
  <div class="partner" style="left:112px">Norvane</div>
  <div class="partner" style="left:311px">Tavrin</div>
  <div class="partner" style="left:511px">Quillmark</div>
  <div class="partner" style="left:708px">Wideharbor</div>
  <div class="partner" style="left:907px">Kestrel Fuel</div>
  <svg class="abs" style="left:1136px;top:80px" width="18" height="56"><path d="M2 2l14 26L2 54" stroke="#ccc" stroke-width="2" fill="none"/></svg>
</section>

<footer class="site-footer">
  <div class="abs foot-brand"><div class="brand-square"></div><div class="brand-name">Meridale Bidding Collective</div></div>
  <p class="abs foot-about">Meridale Bidding Collective is a full-service asset-management company specializing in food manufacturing and packaging equipment. Our goal at Meridale Bidding Collective is to provide our customers with a range of options to liquidate their assets.</p>

  <h3 class="abs foot-h" style="left:488px;top:68px">CONTACT US</h3>
  <svg class="contact-ico" style="top:128px" width="18" height="22"><path d="M9 21s7-7 7-12A7 7 0 0 0 2 9c0 5 7 12 7 12z" stroke="#fff" stroke-width="1.6" fill="none"/><circle cx="9" cy="9" r="2.5" stroke="#fff" stroke-width="1.6" fill="none"/></svg>
  <div class="contact-line" style="top:124px">Meridale Bidding Collective<br>48 Orchard Lane<br>Fairmont, ND 58000</div>
  <svg class="contact-ico" style="top:210px" width="20" height="20"><path d="M4 2l4 1 1 4-2 2a11 11 0 0 0 5 5l2-2 4 1 1 4-3 2C9 19 1 11 2 5z" stroke="#fff" stroke-width="1.5" fill="none"/></svg>
  <div class="contact-line" style="top:208px">Phone :<br>(701) 555-0142</div>
  <svg class="contact-ico" style="top:282px" width="22" height="16"><rect x="1" y="1" width="20" height="14" stroke="#fff" stroke-width="1.5" fill="none"/><path d="M1 1l10 8 10-8" stroke="#fff" stroke-width="1.5" fill="none"/></svg>
  <div class="contact-line" style="top:278px">Email :<br>info@meridale.example</div>

  <h3 class="abs foot-h" style="left:766px;top:65px">SIGN UP TO RECEIVE EMAIL</h3>
  <p class="abs foot-signup">Excepteur sint occaecat cupidatat non proident, sunt in culpa qui nemo enim ipsam</p>
  <div class="abs foot-input">Enter Email</div>
  <a class="abs btn foot-sub">SUBSCRIBE</a>

  <div class="abs foot-rule"></div>
  <span class="social" style="left:514px"></span>
  <span class="social" style="left:560px"></span>
  <span class="social" style="left:604px"></span>
  <span class="social" style="left:646px"></span>
  <p class="abs copyright">Copyright © Meridale Bidding Collective 2021. All rights reserved.</p>
</footer>

</body>
</html>
```